Bref créative
Norland Equity Partners
Investing
Professional
Tom Radcliffe
President
728 Maplewood Ave. Suite 310
Oak Terrace, CA 90418
tom@NorlandEquityPartners.com
www.NorlandEquityPartners.com
We want our logo to be the main component of the card. Have fun and let me see what you got!
Feel free to try 1 or 2 sided card ideas.
Can use other fonts besides the logo font if you desire.

```html
<!DOCTYPE html>
<html lang="en">
<head>
<meta charset="utf-8">
<title>Norland Equity Partners – Business Cards</title>
<link rel="stylesheet" href="https://fonts.googleapis.com/css2?family=Montserrat:wght@600&family=Open+Sans:wght@400;600&display=swap">
<style>
  :root {
    --backdrop: #2c3441;
    --card: #ffffff;
    --accent-red: #e3262b;
    --band-dark: #2b2b2d;
    --ink: #2a2a2a;
    --rule: #3a3a3a;
  }
  * { box-sizing: border-box; margin: 0; padding: 0; }
  html, body {
    width: 1200px; height: 878px; overflow: hidden;
    background: var(--backdrop);
    font-family: "Open Sans", Arial, sans-serif;
  }
  .stage {
    width: 1200px; height: 878px;
    display: flex; align-items: center; justify-content: center; gap: 60px;
  }
  .card {
    position: relative;
    width: 520px; height: 300px;
    background: var(--card);
    border-radius: 16px;
    overflow: hidden;
    box-shadow: 0 10px 30px rgba(0,0,0,.35);
  }
  .edge-red {
    position: absolute; left: 0; top: 0; bottom: 0; width: 24px;
    background: var(--accent-red);
  }
  .edge-red::after {
    content: ""; position: absolute; top: 0; bottom: 0; left: 30px;
    width: 2px; background: var(--band-dark);
  }
  .edge-dark {
    position: absolute; right: 0; top: 0; bottom: 0; width: 42px;
    background: var(--band-dark);
  }
  .edge-dark::before {
    content: ""; position: absolute; top: 0; bottom: 0; left: -8px;
    width: 2px; background: var(--band-dark);
  }
  .brand { display: flex; align-items: center; gap: 12px; }
  .brand-dot {
    width: 46px; height: 46px; border-radius: 50%;
    background: var(--accent-red); flex: none;
  }
  .brand-name {
    font-family: "Montserrat", Arial, sans-serif;
    font-weight: 600; color: var(--ink);
    letter-spacing: .06em; text-transform: uppercase;
  }
  /* Front: contact side */
  .card-front .brand { position: absolute; left: 62px; top: 34px; }
  .card-front .brand-name { font-size: 17px; }
  .card-front .brand-rule {
    position: absolute; left: 62px; right: 80px; top: 94px;
    height: 2px; background: var(--rule);
  }
  .person { position: absolute; left: 62px; top: 106px; line-height: 1.15; }
  .person-name { color: var(--accent-red); font-size: 24px; font-weight: 400; }
  .person-title { color: var(--ink); font-size: 19px; }
  .contact {
    position: absolute; left: 62px; top: 180px;
    list-style: none; color: var(--ink); font-size: 13.5px; line-height: 1.45;
  }
  /* Back: brand side */
  .card-back .brand { position: absolute; left: 62px; top: 76px; }
  .card-back .brand-dot { width: 70px; height: 70px; }
  .card-back .brand-name { font-size: 22px; line-height: 1.2; }
  .card-back .brand-rule {
    position: absolute; left: 62px; right: 80px; top: 172px;
    height: 2px; background: var(--rule);
  }
  .web {
    position: absolute; right: 70px; bottom: 36px;
    color: var(--ink); font-size: 17px; font-weight: 600;
  }
</style>
</head>
<body>
<main class="stage">
  <article class="card card-front">
    <div class="edge-red"></div>
    <div class="edge-dark"></div>
    <div class="brand">
      <span class="brand-dot"></span>
      <span class="brand-name">Norland Equity Partners</span>
    </div>
    <div class="brand-rule"></div>
    <div class="person">
      <p class="person-name">Tom Radcliffe</p>
      <p class="person-title">President</p>
    </div>
    <ul class="contact">
      <li>Address: 728 Maplewood Ave. Suite 310</li>
      <li>Oak Terrace, CA 90418</li>
      <li>Phone: 555-014-2260</li>
      <li>E-mail: tom@NorlandEquityPartners.com</li>
      <li>Web: www.NorlandEquityPartners.com</li>
    </ul>
  </article>

  <article class="card card-back">
    <div class="edge-red"></div>
    <div class="edge-dark"></div>
    <div class="brand">
      <span class="brand-dot"></span>
      <span class="brand-name">Norland Equity<br>Partners</span>
    </div>
    <div class="brand-rule"></div>
    <p class="web">www.NorlandEquityPartners.com</p>
  </article>
</main>
</body>
</html>
```